Business Card Design

I am starting my therapy private practice. I will be an in home therapist, so I go into family's homes instead of using an office to do family/marriage therapy. Therefore, I do not have an office address. I am looking for something in the black, red, gray, and blue color scheme that appeals to both families, couples and teenagers.

Industry/Entity Type

Business

Contact Information for Business Card

Lena Brightwell, MS, MFT Intern
Marriage and Family Therapy
In Home Therapist
617-482-5190
Lena@LenaBrightwell-example.com

```html
<!DOCTYPE html>
<html lang="en">
<head>
<meta charset="UTF-8">
<title>Lena Brightwell – Business Card</title>
<link rel="stylesheet" href="https://fonts.googleapis.com/css2?family=Marcellus+SC&family=Open+Sans:ital,wght@0,400;0,600;1,400&display=swap">
<style>
  :root {
    --page: #e9e7e3;
    --card: #2a2b2d;
    --card-edge: #1f2022;
    --red: #6e0a10;
    --red-deep: #3e0306;
    --red-line: #8a121a;
    --text: #f4f4f4;
    --muted: #cfcfcf;
    --figure: #45474a;
  }
  html, body {
    margin: 0;
    width: 1200px;
    height: 1000px;
    overflow: hidden;
    background: var(--page);
  }
  .business-card {
    position: absolute;
    left: 100px;
    top: 214px;
    width: 1000px;
    height: 572px;
    background: radial-gradient(ellipse at 40% 40%, #323336 0%, var(--card) 55%, var(--card-edge) 100%);
    box-shadow: 0 10px 30px rgba(0,0,0,0.25);
    overflow: hidden;
    font-family: "Open Sans", Arial, sans-serif;
    color: var(--text);
  }
  .rule {
    position: absolute;
    left: 0;
    right: 0;
    height: 2px;
    background: var(--red-line);
  }
  .rule-top { top: 34px; }
  .rule-under { top: 104px; }
  .services {
    position: absolute;
    right: 40px;
    top: 48px;
    margin: 0;
    font-size: 32px;
    font-style: italic;
    letter-spacing: 0.3px;
    white-space: nowrap;
  }
  .services .dot { color: var(--red-line); font-style: normal; padding: 0 6px; }
  .family-figure {
    position: absolute;
    left: 150px;
    top: 130px;
    width: 280px;
    height: 300px;
    background: radial-gradient(ellipse at 50% 55%, var(--figure) 0%, rgba(69,71,74,0.5) 55%, rgba(69,71,74,0) 75%);
  }
  .accent-block {
    position: absolute;
    left: 70px;
    top: 250px;
    width: 100px;
    height: 42px;
    background: var(--red);
  }
  .accent-band {
    position: absolute;
    left: 420px;
    top: 338px;
    width: 600px;
    height: 62px;
    background: linear-gradient(180deg, var(--red) 0%, var(--red-deep) 100%);
  }
  .identity {
    position: absolute;
    right: 60px;
    top: 236px;
    text-align: right;
  }
  .identity .name {
    margin: 0;
    font-family: "Marcellus SC", Georgia, serif;
    font-size: 48px;
    font-weight: 400;
    letter-spacing: 2px;
    line-height: 1;
    white-space: nowrap;
    text-shadow: 0 2px 3px rgba(0,0,0,0.6);
  }
  .identity .credential {
    display: inline-block;
    margin-top: 4px;
    padding: 0 20px 4px 40px;
    font-family: "Marcellus SC", Georgia, serif;
    font-size: 20px;
    color: var(--muted);
    border-bottom: 2px solid var(--red-line);
  }
  .contact-icon { position: absolute; }
  .contact-text {
    position: absolute;
    font-size: 31px;
    line-height: 1.2;
    white-space: nowrap;
  }
  .phone-icon { left: 34px; top: 300px; }
  .phone-text { left: 106px; top: 310px; }
  .email-icon { left: 410px; top: 414px; }
  .email-text { left: 478px; top: 456px; font-size: 29px; }
</style>
</head>
<body>
  <section class="business-card">
    <div class="rule rule-top"></div>
    <p class="services">Marriage and Family Therapy<span class="dot">•</span>In Home Therapist</p>
    <div class="rule rule-under"></div>

    <div class="family-figure" role="img" aria-label="Faint silhouette of a family of four holding hands"></div>

    <div class="accent-block"></div>
    <div class="accent-band"></div>

    <div class="identity">
      <h1 class="name">Lena Brightwell</h1>
      <div class="credential">MS, MFT Intern</div>
    </div>

    <svg class="contact-icon phone-icon" width="54" height="48" viewBox="0 0 54 48" aria-hidden="true">
      <path d="M4 14 C4 4 50 4 50 14 L50 20 L38 20 L38 14 L16 14 L16 20 L4 20 Z" fill="var(--red)"/>
      <path d="M12 22 L42 22 L48 44 L6 44 Z" fill="var(--red)"/>
      <circle cx="27" cy="33" r="6" fill="var(--card)"/>
    </svg>
    <span class="contact-text phone-text">617-482-5190</span>

    <svg class="contact-icon email-icon" width="58" height="50" viewBox="0 0 58 50" aria-hidden="true">
      <path d="M4 20 L29 4 L54 20 L54 46 L4 46 Z" fill="var(--red)"/>
      <path d="M4 20 L29 34 L54 20" fill="none" stroke="var(--card)" stroke-width="3"/>
    </svg>
    <span class="contact-text email-text">Lena@LenaBrightwell-example.com</span>
  </section>
</body>
</html>
```